KLV Home Loans Website

Need a web site designed for a Professional Mortgage company along the lines of the draft site www.klvhomeloans.com.au

The main purpose of the site is to provide a professional image of the company and capture email address's and send out simple messages. ie "INTEREST RATE SPECIAL 4.5% FOR THE MONTH OF JUNE" or whatever...basically short punchy messages to hook people.

The content is important but a lot of that can be provided by links to our lender panel, several of which have been set up.

Most people will want to know current interest rates, and how much they can borrow along with what it will cost. There are various calculators embedded in the lenders sites such as "Repayment Calculators" Borrow Capacity Calculators" Stamp Duty Calculators"

These would be nice to have on site, but if to costly or difficult to start the links can suffice.

The site will need to be updated/amended regularily.

Example "Interest Rate Special" or "Current Special Offer" sections would be required and would need to be easyily editable and in fact would need to be able to switch them off if there is no special running.

Target Market(s)

Target market is a broad spectrum of people from young couple buying first home to older couples investing.

Industry/Entity Type

It Company

Requirements
Must have
• email capture, preferably need to enter email to enter site.

```html
<!DOCTYPE html>
<html lang="en">
<head>
<meta charset="utf-8">
<title>KLV Home Loans</title>
<link rel="stylesheet" href="https://fonts.googleapis.com/css2?family=Noto+Sans:ital,wght@0,400;0,700;1,400&family=Open+Sans:wght@600;700&display=swap">
<style>
:root{
  --page:#202020;
  --panel:#efefef;
  --panel-head:#cacaca;
  --ink:#111111;
  --nav:#f2f2f2;
  --field:#ffffff;
  --field-line:#a9a9a9;
  --btn-top:#8c8c8c;
  --btn-bottom:#4a4a4a;
  --brand:#ffffff;
  --ring:#9aa0ab;
}
*{box-sizing:border-box;margin:0;padding:0}
html,body{width:1200px;height:766px;overflow:hidden;background:var(--page)}
body{position:relative;font-family:Verdana,"Noto Sans",sans-serif;color:var(--ink);font-size:14px}
.brand{position:absolute;left:252px;top:27px;height:133px;display:flex;align-items:center;gap:14px}
.brand-mark{width:70px;height:70px;border-radius:50%;background:var(--ring)}
.brand-name{font-family:"Open Sans",sans-serif;font-weight:700;font-size:40px;color:var(--brand);line-height:1}
.main-nav{position:absolute;right:283px;top:40px;text-align:right;list-style:none}
.main-nav li{font-size:15px;line-height:18.6px;color:var(--nav)}
.panel{position:absolute;left:252px;width:665px;background:var(--panel);border-radius:5px}
.signup{top:177px;height:96px}
.signup-title{position:absolute;top:7px;width:100%;text-align:center;font-weight:700;font-size:15px}
.email-field{position:absolute;left:175px;top:43px;width:211px;height:27px;background:var(--field);border-top:1px solid var(--field-line);border-left:1px solid var(--field-line);font-family:Arial,"Noto Sans",sans-serif;font-size:14.5px;color:#777;padding:4px 6px}
.btn{position:absolute;border-radius:4px;border:1px solid #9a9a9a;background:linear-gradient(var(--btn-top),var(--btn-bottom));color:#fff;font-family:Arial,"Noto Sans",sans-serif;font-weight:700;font-size:13px;display:flex;align-items:center;padding-left:9px;text-shadow:0 1px 1px #000}
.signup .btn{left:402px;top:41px;width:88px;height:34px}
.tagline{top:291px;height:51px;text-align:center;font-size:14.5px;line-height:18.6px;padding-top:7px}
.tagline strong{font-size:15px}
.intro{top:360px;height:107px;padding:7px 7px;font-size:14.3px;line-height:18.6px;text-align:justify;letter-spacing:.15px}
.calculator{top:485px;height:162px;border:1px solid #d8d8d8;overflow:hidden}
.calc-head{height:29px;background:var(--panel-head);font-weight:700;font-size:15px;padding:5px 6px}
.lbl{position:absolute;font-size:14.3px}
.input{position:absolute;background:var(--field);border-top:1px solid var(--field-line);border-left:1px solid var(--field-line);font-size:14px;padding:4px 6px;height:27px}
.unit{position:absolute;font-size:14.5px;font-style:italic}
.explain{position:absolute;left:6px;top:124px;font-weight:700;font-size:14.5px}
.check-row{position:absolute;left:10px;top:142px;display:flex;align-items:center;gap:7px;font-size:14.3px}
.calculator .btn{left:481px;top:111px;width:88px;height:42px;font-size:13px}
</style>
</head>
<body>
<header>
  <div class="brand"><span class="brand-mark"></span><span class="brand-name">KLV Home Loans</span></div>
  <ul class="main-nav">
    <li>Home</li><li>About Us</li><li>Our Clients</li><li>Services</li><li>Our Partners</li><li>E-Mail</li>
  </ul>
</header>

<section class="panel signup">
  <p class="signup-title">Join our mailing list for industry news and special offers!</p>
  <div class="email-field">Enter your e-mail address here</div>
  <div class="btn">Submit</div>
</section>

<section class="panel tagline">
  <strong>Time Is Valuable!</strong><br>
  KLV can save your valuable time with fast, reliable and quality loan products.
</section>

<section class="panel intro">
  <strong>KLV Home Loans Services</strong> offers a complete range of Mortgage and Loan products to suit our individual clients needs. Whether you are a First Home Buyer, Up-Sizing or Down-Sizing, Refinancing, Investing or simply want a new car or equipment purchase, contact us for a no obligation assessment and get the latest information on the available products to suit your needs.
</section>

<section class="panel calculator">
  <div class="calc-head">Purchase &amp; Financing Information</div>
  <span class="lbl" style="left:6px;top:39px">Sale Price of Home:</span>
  <div class="input" style="left:192px;top:34px;width:91px">150000</div>
  <span class="unit" style="left:290px;top:37px">(In Dollars)</span>
  <span class="lbl" style="left:393px;top:39px">Percentage Down:</span>
  <div class="input" style="left:579px;top:34px;width:40px">10</div>
  <span class="unit" style="left:631px;top:37px">%</span>

  <span class="lbl" style="left:6px;top:77px">Length of Mortgage:</span>
  <div class="input" style="left:192px;top:72px;width:91px">30</div>
  <span class="unit" style="left:290px;top:75px">Years</span>
  <span class="lbl" style="left:393px;top:77px">Annual Interest Rate:</span>
  <div class="input" style="left:579px;top:72px;width:40px">7</div>
  <span class="unit" style="left:631px;top:75px">%</span>

  <p class="explain">Explain Calculations:</p>
  <div class="check-row">
    <svg width="12" height="12" viewBox="0 0 12 12" aria-hidden="true"><rect x=".5" y=".5" width="11" height="11" fill="#fff" stroke="#333"/><path d="M2.5 6.2l2.3 2.3 4.7-5" fill="none" stroke="#111" stroke-width="1.6"/></svg>
    <span>Show me the calculations and amortization</span>
  </div>
  <div class="btn">Calculate</div>
</section>
</body>
</html>
```